strength and conditioning business needs a brochure

We are after a simple yet bold brochure design that uses base colours of red, white, black and grey. We have supporting text that we would like incorporated to see how it all looks as a finished product, as well as the logo.
Reason: To give designers a last chance to make recommended changes before choice is made.

```html
<!DOCTYPE html>
<html lang="en">
<head>
<meta charset="utf-8">
<title>Iron Method Institute – Brochure</title>
<link rel="stylesheet" href="https://fonts.googleapis.com/css2?family=Source+Sans+3:wght@400;600;700&display=swap">
<style>
:root{
  --stage:#c1b298;
  --stage-edge:#6f6a60;
  --slate:#4a4b4d;
  --slate-dark:#353638;
  --red:#d0202a;
  --red-dark:#8e1016;
  --ink:#2b2b2b;
  --text-soft:#c9c9c9;
  --text-bright:#ffffff;
  --paper:#ffffff;
}
*{box-sizing:border-box;margin:0;padding:0}
html,body{width:1200px;height:530px;overflow:hidden}
body{background:var(--stage);font-family:"Source Sans 3",Arial,sans-serif;position:relative}
.stage-frame{position:absolute;left:4px;top:4px;width:1192px;height:522px;border:1px solid var(--stage-edge)}
.panel{position:absolute;top:53px;width:531px;height:415px;background:var(--paper);overflow:hidden}
.panel--inside{left:62px}
.panel--outside{left:612px}
.panel__field{position:absolute;left:0;top:0;width:100%;height:357px;
  background:radial-gradient(ellipse at 40% 30%,var(--slate) 0%,var(--slate-dark) 100%)}
.col{position:absolute;color:var(--text-soft);font-size:8.4px;line-height:11px}
.col--justified{text-align:justify}
.col p{margin-bottom:9px}
.col .lead{color:var(--text-bright);font-weight:700}
.topic-list{list-style:none}
.topic-list li{position:relative;padding-left:9px;margin-bottom:9px}
.topic-list li::before{content:"";position:absolute;left:0;top:4px;width:3px;height:3px;border-radius:50%;background:#8c8c8c}
.ribbon{position:absolute;height:22px;background:var(--red);color:var(--text-bright);
  font-weight:600;font-size:13px;letter-spacing:.3px;display:flex;align-items:center;justify-content:center;
  box-shadow:2px 2px 0 var(--red-dark)}
.band{position:absolute;left:0;top:327px;width:100%;height:32px}
.band__label{position:absolute;left:0;top:327px;width:100%;height:30px;color:var(--text-bright);
  font-weight:600;font-size:13px;letter-spacing:.4px;display:flex;align-items:center;justify-content:center}
.brand{position:absolute;left:0;top:375px;width:100%;display:flex;align-items:center;justify-content:center;gap:6px}
.brand__mark{width:9px;height:9px;background:var(--red)}
.brand__name{font-weight:700;font-size:10px;letter-spacing:1px;color:var(--ink)}
.join-visual{position:absolute;left:408px;top:80px;width:52px;height:52px;
  background:linear-gradient(160deg,#5a5b5e 0%,#3c3d40 100%)}
.badge{position:absolute;left:366px;top:172px;width:142px;height:20px;background:var(--paper);
  display:flex;align-items:center;justify-content:center;gap:5px;box-shadow:2px 2px 0 #aaa}
.badge .brand__name{font-size:8.5px}
.email{color:var(--text-bright);font-weight:700}
</style>
</head>
<body>
<div class="stage-frame"></div>

<section class="panel panel--inside">
  <div class="panel__field" role="img" aria-label="Dark grey faceted geometric background texture"></div>

  <div class="ribbon" style="left:18px;top:27px;width:135px">ABOUT US</div>
  <div class="col" style="left:22px;top:58px;width:146px">
    <p class="lead">Iron Method Institute (IMI) is an educational resource dedicated to providing coaches, trainers and trainees with the best information available in the areas of strength and body recomposition (muscle gain and fat loss).</p>
    <p>Each month 2-4 in-depth articles are posted from one of the following areas:</p>
    <ul class="topic-list">
      <li>1. Psychology/Philosophy</li>
      <li>2. Exercises (in depth analysis of how to perform exercises with videos of athletes actually performing a work set)</li>
      <li>3. Programming/Training (intensity, volume, frequency, periodization etc.)</li>
      <li>4. Diet</li>
    </ul>
  </div>

  <div class="col" style="left:196px;top:32px;width:150px">
    <ul class="topic-list">
      <li>5. Recovery (all methods to enhance recovery e.g. foam rolling, sleep etc.)</li>
      <li>6. Product Review (reviews of any products like books that would be useful, especially for coaches/trainers)</li>
      <li>7. Research/Statistics (boring yes but vital if you want to learn to read research and apply it appropriately)</li>
      <li>8. Coach/Trainer (issues that specifically face coaches and trainers)</li>
    </ul>
    <p style="margin-top:26px">In addition to the articles released every month, a discussion forum will be open where any questions and topics can be asked/discussed. It will also be an opportunity for fellow coaches/trainers to network.</p>
  </div>

  <div class="col col--justified" style="left:370px;top:32px;width:140px">
    <p>IMI can be purchased as either a monthly subscription ($10 per month) or a yearly one ($100) which gives full access to all content that has been released up until the time of joining.</p>
  </div>
  <div class="ribbon" style="left:362px;top:118px;width:160px">WHY CHOOSE IMI???</div>
  <div class="col" style="left:370px;top:152px;width:148px">
    <p>Scientific: Every article that is written takes into account the latest research available in the scientific literature, providing you with the best information that science can currently offer.</p>
    <p>Practicality: While scientifically based, every article that is written also relies on observation, personal experiences of others and tacit knowledge (knowledge obtained from doing).</p>
    <p>Integrity: IMI prides itself on being an objective source. No affiliations do</p>
  </div>

  <svg class="band" viewBox="0 0 531 32" aria-hidden="true">
    <polygon points="8,8 22,8 22,32" fill="var(--red-dark)"/>
    <polygon points="523,8 509,8 509,32" fill="var(--red-dark)"/>
    <rect x="22" y="0" width="487" height="30" fill="var(--red)"/>
    <polygon points="0,4 22,4 22,30 0,30 8,17" fill="var(--red)"/>
    <polygon points="531,4 509,4 509,30 531,30 523,17" fill="var(--red)"/>
  </svg>
  <div class="band__label">"KNOWLEDGE IS POWER"</div>

  <div class="brand"><span class="brand__mark"></span><span class="brand__name">IRON METHOD INSTITUTE</span></div>
</section>

<section class="panel panel--outside">
  <div class="panel__field" role="img" aria-label="Dark grey faceted geometric background texture"></div>

  <div class="col col--justified" style="left:25px;top:32px;width:134px">
    <p>or will exist with other businesses to remove the possibility of any bias or hidden agendas (which are more common than most think).</p>
    <p>Support: Whether you are a seasoned coach/trainer, just getting started or simply want to know more about how best to optimise your training, diet and mental approach, support will always be available through the group's forum where questions can be asked and answered.</p>
    <p>Cost: At $10 a month, this is a very cost effective strategy for coaches, trainers and trainees alike to improve their knowledge without breaking the budget. In fact, knowledge gained from IMI will likely SAVE you money in the long term.</p>
  </div>

  <div class="ribbon" style="left:191px;top:27px;width:148px">HOW TO JOIN</div>
  <div class="col" style="left:198px;top:62px;width:148px">
    <p>IMI is a subscription-based resource but you are not locked in to any contracts. In fact, at any time you want you can cancel your subscription, no questions asked.</p>
    <p>To join, send us an email to the address below and we will walk you through the very simple steps to join:</p>
    <p class="email" style="margin-top:14px">hello@ironmethodinstitute.com</p>
  </div>

  <div class="join-visual" role="img" aria-label="Place for a training equipment icon"></div>

  <div class="badge"><span class="brand__mark" style="width:7px;height:7px"></span><span class="brand__name">IRON METHOD INSTITUTE</span></div>

  <svg class="band" viewBox="0 0 531 32" aria-hidden="true">
    <rect x="0" y="0" width="531" height="30" fill="var(--red)"/>
  </svg>
  <div class="band__label">"KNOWLEDGE IS POWER"</div>

  <div class="brand"><span class="brand__mark"></span><span class="brand__name">IRON METHOD INSTITUTE</span></div>
</section>
</body>
</html>
```